Business card for our large format printing and installation business

We want a professional looking business card for our business. We manufacture and install Signs.

On the back of the card add this info
Large Format Graphics Printing & Installations, Event Graphics, Banners, Posters, Vehicle Fleet Graphics, Boat Wraps, Wall Murals, Decals,Displays,Signs,Plaques,Digital Signs

On the Front of the card add the Tallowfern Signs logo, plus On the back of the card add the Orange Tallowfern Wraps logo. The 2 vector logos are attached to the design brief.

Target Market(s)

Local business owners

Contact Information for Business Card

Colors
f37122
f68d4e
f9ba93

Requirements
Must have
• On the Front of the card add the Tallowfern Signs logo, plus On the back of the card add the Orange Tallowfern Wraps logo. The 2 vector logos are attached to the design brief.

```html
<!DOCTYPE html>
<html lang="en">
<head>
<meta charset="utf-8">
<title>Tallowfern Signs – Business Card</title>
<link href="https://fonts.googleapis.com/css2?family=Poppins:wght@400;500;800&display=swap" rel="stylesheet">
<style>
  :root {
    --page: #ffffff;
    --card-black: #050505;
    --card-orange: #f68d4e;
    --accent: #f37122;
    --accent-soft: #f9ba93;
    --logo-gold: #f6b21c;
    --ink-white: #ffffff;
    --ink-dark: #141414;
  }
  * { box-sizing: border-box; margin: 0; padding: 0; }
  html, body { width: 960px; height: 1200px; overflow: hidden; background: var(--page); }
  body { font-family: "Poppins", sans-serif; position: relative; }

  .card {
    position: absolute; left: 80px; width: 800px; height: 457px;
    box-shadow: 0 8px 18px rgba(0,0,0,0.35);
  }
  .card-front { top: 80px; background: var(--card-black); color: var(--ink-white); }
  .card-back { top: 597px; background: var(--card-orange); color: var(--ink-white); }

  .logo-name {
    position: absolute; font-weight: 800; line-height: 1; letter-spacing: -0.5px;
  }
  .card-front .logo-name { left: 40px; top: 58px; font-size: 40px; color: var(--logo-gold); }
  .card-front .logo-name span { display: block; padding-left: 88px; font-size: 30px; }
  .card-back .logo-name { left: 34px; top: 34px; font-size: 34px; color: var(--ink-dark); }
  .card-back .logo-name span { display: block; padding-left: 76px; font-size: 24px; }

  .website { position: absolute; right: 86px; top: 108px; font-size: 21px; }

  .person { position: absolute; left: 40px; top: 204px; }
  .person-name { font-size: 25px; color: var(--accent); line-height: 1.1; }
  .person-title { font-size: 23px; line-height: 1.1; }

  .divider {
    position: absolute; left: 254px; right: 26px; top: 222px;
    border-top: 3px dashed var(--accent);
  }

  .contacts { position: absolute; right: 82px; top: 254px; text-align: right; list-style: none; }
  .contacts li { font-size: 20px; line-height: 34px; display: flex; justify-content: flex-end; align-items: center; gap: 6px; }
  .contacts svg { width: 18px; height: 18px; }

  .address { position: absolute; right: 84px; top: 363px; font-size: 20px; color: var(--accent); }

  .services { position: absolute; left: 150px; top: 192px; width: 560px; display: grid;
    grid-template-columns: 250px 1fr; row-gap: 6px; list-style: none; }
  .services li { font-size: 18px; line-height: 28px; display: flex; align-items: center; gap: 12px; }
  .services li.wide { grid-column: 1 / 3; }
  .services svg { width: 22px; height: 22px; flex: none; }
</style>
</head>
<body>
  <section class="card card-front" aria-label="Card front">
    <div class="logo-name">Tallowfern<span>Signs</span></div>
    <p class="website">www.tallowfernwraps.com</p>
    <div class="person">
      <p class="person-name">Marcus Ellery</p>
      <p class="person-title">CEO</p>
    </div>
    <div class="divider"></div>
    <ul class="contacts">
      <li>555-301-4827
        <svg viewBox="0 0 20 20"><path d="M5 3l3 0 1 4-2 1.5a9 9 0 0 0 4.5 4.5L13 11l4 1v3a2 2 0 0 1-2 2C8 17 3 12 3 5a2 2 0 0 1 2-2z" fill="none" stroke="#f37122" stroke-width="1.8"/></svg>
      </li>
      <li>555-268-9143
        <svg viewBox="0 0 20 20"><circle cx="10" cy="10" r="8.5" fill="#f37122"/><rect x="6" y="6" width="8" height="8" rx="1.5" fill="#050505"/></svg>
      </li>
      <li>marcus@tallowfern.net
        <svg viewBox="0 0 20 20"><circle cx="10" cy="10" r="8.5" fill="#f37122"/><rect x="5.5" y="7" width="9" height="6" fill="#050505"/><path d="M5.5 7l4.5 3.5L14.5 7" stroke="#f37122" stroke-width="1" fill="none"/></svg>
      </li>
    </ul>
    <p class="address">1480 Harbor View Lane #7, Seabrook Point, FL 33120</p>
  </section>

  <section class="card card-back" aria-label="Card back">
    <div class="logo-name">Tallowfern<span>Wraps</span></div>
    <ul class="services">
      <li class="wide"><svg viewBox="0 0 22 22"><circle cx="11" cy="11" r="8" fill="none" stroke="#141414" stroke-width="1.6"/><path d="M7 11l3 3 9-10" fill="none" stroke="#141414" stroke-width="2"/></svg>Large Format Graphics Printing &amp; Installations</li>
      <li><svg viewBox="0 0 22 22"><circle cx="11" cy="11" r="8" fill="none" stroke="#141414" stroke-width="1.6"/><path d="M7 11l3 3 9-10" fill="none" stroke="#141414" stroke-width="2"/></svg>Event Graphics</li>
      <li><svg viewBox="0 0 22 22"><circle cx="11" cy="11" r="8" fill="none" stroke="#141414" stroke-width="1.6"/><path d="M7 11l3 3 9-10" fill="none" stroke="#141414" stroke-width="2"/></svg>Digital Signs</li>
      <li><svg viewBox="0 0 22 22"><circle cx="11" cy="11" r="8" fill="none" stroke="#141414" stroke-width="1.6"/><path d="M7 11l3 3 9-10" fill="none" stroke="#141414" stroke-width="2"/></svg>Banners</li>
      <li><svg viewBox="0 0 22 22"><circle cx="11" cy="11" r="8" fill="none" stroke="#141414" stroke-width="1.6"/><path d="M7 11l3 3 9-10" fill="none" stroke="#141414" stroke-width="2"/></svg>Vehicle Fleet Graphics,</li>
      <li><svg viewBox="0 0 22 22"><circle cx="11" cy="11" r="8" fill="none" stroke="#141414" stroke-width="1.6"/><path d="M7 11l3 3 9-10" fill="none" stroke="#141414" stroke-width="2"/></svg>Boat Wraps</li>
      <li><svg viewBox="0 0 22 22"><circle cx="11" cy="11" r="8" fill="none" stroke="#141414" stroke-width="1.6"/><path d="M7 11l3 3 9-10" fill="none" stroke="#141414" stroke-width="2"/></svg>Posters</li>
      <li><svg viewBox="0 0 22 22"><circle cx="11" cy="11" r="8" fill="none" stroke="#141414" stroke-width="1.6"/><path d="M7 11l3 3 9-10" fill="none" stroke="#141414" stroke-width="2"/></svg>Plaques</li>
      <li><svg viewBox="0 0 22 22"><circle cx="11" cy="11" r="8" fill="none" stroke="#141414" stroke-width="1.6"/><path d="M7 11l3 3 9-10" fill="none" stroke="#141414" stroke-width="2"/></svg>Wall Murals</li>
      <li><svg viewBox="0 0 22 22"><circle cx="11" cy="11" r="8" fill="none" stroke="#141414" stroke-width="1.6"/><path d="M7 11l3 3 9-10" fill="none" stroke="#141414" stroke-width="2"/></svg>Decals</li>
      <li><svg viewBox="0 0 22 22"><circle cx="11" cy="11" r="8" fill="none" stroke="#141414" stroke-width="1.6"/><path d="M7 11l3 3 9-10" fill="none" stroke="#141414" stroke-width="2"/></svg>Displays &amp; Signs</li>
    </ul>
  </section>
</body>
</html>
```